Letterhead/Envelope Design Project

We are a 501c3 non-profit that supports educational programs at Dunmoral Fern Hollow State Park in California. We have new logo and need letterhead. The design needs need incorporate the logo attached. It needs to contain the information in document attached called "information" attached. Please see our website fernhollow.org to get the feeling and colors we are looking for.

```html
<!DOCTYPE html>
<html lang="en">
<head>
<meta charset="utf-8">
<title>Dunmoral Fern Hollow Association — Letterhead</title>
<link href="https://fonts.googleapis.com/css2?family=Lato:wght@300&display=swap" rel="stylesheet">
<style>
  :root {
    --paper: #ffffff;
    --forest: #1f4a2a;
    --clay: #d9866c;
    --rule: #e2c7bd;
  }
  html, body {
    margin: 0;
    padding: 0;
    width: 900px;
    height: 1200px;
    overflow: hidden;
    background: var(--paper);
  }
  .letterhead {
    position: relative;
    width: 900px;
    height: 1200px;
    background: var(--paper);
  }
  .brand {
    position: absolute;
    left: 33px;
    top: 36px;
    display: flex;
    align-items: center;
    gap: 12px;
  }
  .brand-mark {
    width: 22px;
    height: 22px;
    background: var(--forest);
    flex: none;
  }
  .brand-name {
    font-family: "Lato", sans-serif;
    font-weight: 300;
    font-size: 18px;
    line-height: 22.7px;
    color: var(--forest);
    margin: 0;
    white-space: nowrap;
  }
  .contact {
    position: absolute;
    left: 617px;
    top: 35px;
    padding-left: 15px;
    border-left: 1px solid var(--rule);
    font-family: "Lato", sans-serif;
    font-weight: 300;
    font-size: 18px;
    line-height: 22.7px;
    color: var(--clay);
    font-style: normal;
  }
  .contact p { margin: 0; white-space: nowrap; }
</style>
</head>
<body>
  <main class="letterhead">
    <header class="brand">
      <div class="brand-mark"></div>
      <p class="brand-name">Dunmoral Fern Hollow Association</p>
    </header>
    <address class="contact">
      <p>P.O. Box 4820</p>
      <p>Larkmoor, CA 95811-4820</p>
      <p>Phone: 209.555.0148</p>
      <p>Fax: 209.555.0172</p>
      <p>dfha@fernhollow.org</p>
      <p>website: fernhollow.org</p>
    </address>
  </main>
</body>
</html>
```